Business Card Design - TBW (company name)

Over 20 years of progressive technology design, migration and management experience that drives business objectives and streamlines operations. Continuously challenge conventions to meet and exceed business security, availability and functionality requirements. Maintain exceptional vendor relationships to ensure ongoing knowledge of emerging products and to secure preferred service agreements. Recruit and utilize top talent and foster a collegial environment that advances innovation and performance excellence. design logo using 3 arrows of different colors green, gold, blue

Industry/Entity Type

Progressive

Contact Information for Business Card

Martin K. Osgood
IT Strategist / Consultant

626.583.2904 MOsgood@tbwosgood.com 4817 Ferndale Court Pasadena, CA 91107

Colors
0255a3
f37122
fece3e

Requirements
Must have
• Note NEW EMAIL ADDRESS
• MOsgood@tbwosgood.com
• NOTE NEW ORDER of the work I do.
• Infrastructure – Systems – Cybersecurity
Nice to have
• main color should be orange

```html
<!DOCTYPE html>
<html lang="en">
<head>
<meta charset="utf-8">
<title>TBW Business Card – Martin K. Osgood</title>
<link rel="stylesheet" href="https://fonts.googleapis.com/css2?family=Source+Sans+3:ital,wght@0,400;0,600;0,700;1,400&display=swap">
<style>
  :root {
    --backdrop: #1c1c1c;
    --card: #ffffff;
    --blue: #29a3dc;
    --blue-deep: #1b8fcc;
    --green: #17a84b;
    --gold: #f6b91a;
    --white: #ffffff;
  }
  * { box-sizing: border-box; margin: 0; padding: 0; }
  html, body {
    width: 1200px; height: 800px; overflow: hidden;
    background: var(--backdrop);
    font-family: "Source Sans 3", "Myriad Pro", Arial, sans-serif;
  }
  .canvas { position: relative; width: 1200px; height: 800px; }

  .card {
    position: absolute;
    width: 560px; height: 320px;
    background: var(--card);
    overflow: hidden;
    box-shadow: 0 6px 18px rgba(0,0,0,.45);
  }
  .card--front { left: 40px; top: 80px; }
  .card--back  { left: 600px; top: 400px; }

  .card__shape { position: absolute; inset: 0; width: 100%; height: 100%; }

  .brand-name {
    position: absolute;
    font-weight: 700;
    color: var(--blue);
    letter-spacing: 2px;
    line-height: 1;
    display: flex; align-items: center; gap: 12px;
  }
  .brand-name__dot {
    width: 18px; height: 18px; border-radius: 50%;
    background: var(--green);
  }
  .card--front .brand-name { left: 210px; top: 98px; font-size: 64px; }
  .card--back  .brand-name { left: 34px; top: 106px; font-size: 48px; }

  .services { position: absolute; font-weight: 600; white-space: nowrap; line-height: 1.2; }
  .card--front .services { left: 0; right: 0; top: 214px; text-align: center; font-size: 29px; }
  .card--back  .services { right: 26px; top: 124px; font-size: 17px; }
  .services__infra { color: var(--green); }
  .services__systems { color: var(--blue); }
  .services__cyber { color: var(--gold); }
  .services__sep { color: var(--blue); }

  .holder { position: absolute; right: 26px; top: 24px; text-align: right; color: var(--blue); }
  .holder__name { font-size: 20px; font-weight: 700; line-height: 1.2; }
  .holder__title { font-size: 15px; font-style: italic; margin-top: 4px; }

  .contact {
    position: absolute; bottom: 26px;
    color: var(--white); font-size: 17px; line-height: 1.55;
    font-style: normal;
  }
  .contact--address { left: 28px; }
  .contact--reach { right: 26px; text-align: right; }
  .contact__line { display: flex; align-items: center; justify-content: flex-end; gap: 4px; }
  .contact__icon { width: 13px; height: 13px; fill: var(--white); }
</style>
</head>
<body>
<main class="canvas">

  <section class="card card--front" aria-label="Card front">
    <svg class="card__shape" viewBox="0 0 560 320" aria-hidden="true">
      <path d="M0 196 C60 170 150 100 226 0" fill="none" stroke="var(--gold)" stroke-width="7"/>
      <path d="M0 204 C66 178 162 106 240 0" fill="none" stroke="var(--blue)" stroke-width="7"/>
      <path d="M0 212 C72 186 174 112 256 0" fill="none" stroke="var(--green)" stroke-width="8"/>
    </svg>
    <div class="brand-name"><span class="brand-name__dot"></span>TBW</div>
    <p class="services">
      <span class="services__infra">Infrastructure</span>
      <span class="services__sep">•</span>
      <span class="services__systems">Systems</span>
      <span class="services__sep">•</span>
      <span class="services__cyber">Cybersecurity</span>
    </p>
  </section>

  <section class="card card--back" aria-label="Card back">
    <svg class="card__shape" viewBox="0 0 560 320" aria-hidden="true">
      <path d="M0 205 C120 185 220 250 380 238 C470 230 520 205 560 210 L560 320 L0 320 Z" fill="var(--blue)"/>
    </svg>
    <div class="holder">
      <p class="holder__name">Martin K. Osgood</p>
      <p class="holder__title">IT Strategist / Consultant</p>
    </div>
    <div class="brand-name"><span class="brand-name__dot"></span>TBW</div>
    <p class="services">
      <span class="services__infra">Infrastructure</span>
      <span class="services__sep">•</span>
      <span class="services__systems">Systems</span>
      <span class="services__sep">•</span>
      <span class="services__cyber">Cybersecurity</span>
    </p>
    <address class="contact contact--address">
      4817 Ferndale Court<br>Pasadena, CA 91107
    </address>
    <div class="contact contact--reach">
      <p class="contact__line">
        <svg class="contact__icon" viewBox="0 0 24 24" aria-hidden="true"><path d="M6.6 10.8a15.1 15.1 0 0 0 6.6 6.6l2.2-2.2a1 1 0 0 1 1-.25 11.4 11.4 0 0 0 3.6.57 1 1 0 0 1 1 1V20a1 1 0 0 1-1 1A17 17 0 0 1 3 4a1 1 0 0 1 1-1h3.5a1 1 0 0 1 1 1c0 1.25.2 2.45.57 3.57a1 1 0 0 1-.25 1z"/></svg>
        : 626.583.2904
      </p>
      <p class="contact__line">
        <svg class="contact__icon" viewBox="0 0 24 24" aria-hidden="true"><path d="M2 5h20v14H2z M3.5 6.5 12 13l8.5-6.5" stroke="var(--blue)" stroke-width="1.4"/></svg>
        : MOsgood@tbwosgood.com
      </p>
    </div>
  </section>

</main>
</body>
</html>
```